Content Management firm needs a one pager for conference brochure

Harbor Lattice is a sponsor at next month's TideMeet conference (https://tidemeet.org/) and we need a one-page advertisement for the conference's printed program.

Attached is the draft wording and other brochures for inspiration. Feel free to copy the layouts as we want brand consistency. Check out our website too: www.harborlattice.com

For the services with icons at the bottom of the page, check out this website: harborlattice.tech

Target Market(s)

Decision makers looking for content management and documentation optimalization and automation services and technologies.

Industry/Entity Type

Content and Documentation Management

Font styles to use
Sans Serif
Other font styles liked:
• Poppins

Colors
0054AA
0677BA
7BADD7
CADEEF
E8F1F8
E54698
E96AAD
F1A4CE
F9D9EA
FCEFF6

Requirements
Must have
• Project size: 4.5 x 7.5 inches as high-rez PDF

```html
<!DOCTYPE html>
<html lang="en">
<head>
<meta charset="utf-8">
<title>Harbor Lattice – TideMeet Program Advertisement</title>
<link rel="stylesheet" href="https://fonts.googleapis.com/css2?family=Poppins:wght@400;500;600;700;800&display=swap">
<style>
  :root {
    --navy: #2e3192;
    --navy-deep: #2b2f86;
    --royal: #2f5fb5;
    --purple: #9a4f9e;
    --ink: #111111;
    --paper: #f1f1f4;
    --stage: #e4e4e8;
    --white: #ffffff;
    --line: #c9c9d2;
    --footer: #0b0b0b;
  }
  * { box-sizing: border-box; margin: 0; padding: 0; }
  html, body { width: 780px; height: 1200px; overflow: hidden; }
  body {
    background: var(--stage);
    font-family: "Poppins", sans-serif;
    position: relative;
  }
  .flyer {
    position: absolute;
    left: 40px; top: 17px;
    width: 700px; height: 1166px;
    background: var(--paper);
    overflow: hidden;
    box-shadow: 0 6px 18px rgba(0,0,0,.18);
  }
  .abs { position: absolute; }

  /* header */
  .hero-band { left: 0; top: 0; width: 700px; height: 510px; }
  .brand { left: 38px; top: 48px; display: flex; align-items: center; gap: 14px; }
  .brand-dot { width: 52px; height: 52px; border-radius: 50%; background: var(--navy); }
  .brand-name { font-weight: 600; font-size: 30px; color: var(--navy); letter-spacing: -.3px; }
  .hero-art {
    left: 434px; top: 25px; width: 266px; height: 282px;
    border-radius: 14px;
    background: linear-gradient(160deg, rgba(255,255,255,.28), rgba(30,30,40,.55) 70%, rgba(154,79,158,.5));
  }
  .headline {
    left: 39px; top: 152px; width: 420px;
    color: var(--white); font-weight: 800; font-size: 34px; line-height: 40px;
    letter-spacing: -.3px;
  }
  .rule { left: 39px; top: 245px; width: 480px; height: 1px; background: rgba(255,255,255,.4); }
  .rule-accent { left: 64px; top: 243px; width: 70px; height: 5px; border-radius: 3px; background: var(--purple); }
  .subhead {
    left: 39px; top: 260px; width: 420px;
    color: var(--white); font-weight: 600; font-size: 21px; line-height: 28px;
  }
  .intro {
    left: 41px; top: 333px; width: 620px;
    color: var(--white); font-size: 13.3px; line-height: 16.8px; text-align: justify;
  }
  .intro p + p { margin-top: 9px; }

  /* booth */
  .chat-icon { left: 43px; top: 530px; width: 58px; height: 58px; }
  .booth {
    left: 112px; top: 530px; width: 560px;
    color: var(--navy); font-weight: 600; font-size: 24px; line-height: 29px;
  }

  /* talks */
  .tab {
    left: 38px; top: 615px; width: 382px; height: 35px;
    background: var(--purple); border-radius: 0 18px 18px 0;
    color: var(--white); font-weight: 700; font-size: 20px; line-height: 35px; padding-left: 13px;
  }
  .talks { left: 38px; top: 664px; width: 400px; }
  .timeline { position: absolute; left: 5px; top: 6px; width: 2px; height: 196px; background: var(--purple); }
  .talk { position: relative; padding-left: 21px; margin-bottom: 11px; }
  .talk::before {
    content: ""; position: absolute; left: 0; top: 4px;
    width: 12px; height: 12px; border-radius: 50%;
    border: 2.5px solid var(--purple); background: var(--paper);
  }
  .talk-title { font-weight: 600; font-size: 14.5px; line-height: 18.5px; color: var(--ink); }
  .talk-speaker { font-size: 13.5px; line-height: 17px; color: var(--ink); }
  .talk-time { font-weight: 600; font-size: 13.5px; line-height: 20px; color: var(--purple); margin-top: 3px; }
  .collab-art {
    left: 417px; top: 675px; width: 252px; height: 255px; border-radius: 16px;
    background: linear-gradient(150deg, #e6e6ea, #9a4f9e33 45%, #30b98433 70%, #dcdce2);
  }

  /* services */
  .services-title {
    left: 42px; top: 956px; width: 616px; display: flex; align-items: center; gap: 8px;
    color: var(--navy); font-weight: 700; font-size: 19px;
  }
  .services-title .ln { flex: 1; height: 1px; background: var(--line); position: relative; }
  .services-title .ln.left::after, .services-title .ln.right::before {
    content: ""; position: absolute; top: -3px; width: 7px; height: 7px; border-radius: 50%;
    border: 1px solid #999; background: var(--paper);
  }
  .services-title .ln.left::after { right: 0; }
  .services-title .ln.right::before { left: 0; }
  .service { display: flex; align-items: center; gap: 8px; }
  .service-icon {
    width: 45px; height: 45px; border-radius: 50%; flex: none;
    background: radial-gradient(circle at 35% 30%, var(--royal), var(--navy-deep));
    box-shadow: 0 3px 3px rgba(0,0,0,.15);
    display: flex; align-items: center; justify-content: center;
  }
  .service-name { font-size: 13px; line-height: 16px; color: var(--ink); }

  /* footer */
  .footer-band { left: 0; top: 1112px; width: 700px; height: 54px; }
  .contact { color: var(--white); font-size: 13px; display: flex; align-items: center; gap: 6px; top: 1140px; }
  .contact .bullet { width: 14px; height: 14px; border-radius: 50%; background: var(--navy); border: 1.5px solid #6a73d6; }
  .phone { left: 481px; top: 1122px; color: var(--white); font-weight: 600; font-size: 19px; display: flex; align-items: center; gap: 9px; }
  .phone-badge { width: 22px; height: 22px; border-radius: 50%; background: var(--white); display: flex; align-items: center; justify-content: center; }
</style>
</head>
<body>
<main class="flyer">
  <svg class="abs hero-band" viewBox="0 0 700 510" aria-hidden="true">
    <defs>
      <linearGradient id="heroGrad" x1="0" y1="1" x2="1" y2="0">
        <stop offset="0" stop-color="#2b2f86"/>
        <stop offset=".6" stop-color="#2e3a9a"/>
        <stop offset="1" stop-color="#2f62b8"/>
      </linearGradient>
    </defs>
    <path d="M0 122 H262 C285 122 300 112 315 92 L333 68 C345 52 358 46 380 46 H700 V510 H0 Z" fill="url(#heroGrad)"/>
  </svg>

  <div class="abs brand">
    <span class="brand-dot"></span>
    <span class="brand-name">Harbor Lattice</span>
  </div>

  <div class="abs hero-art" role="img" aria-label="Illustration of a humanoid robot rising from a smartphone with a speech bubble and holographic interface"></div>

  <h1 class="abs headline">DOES YOUR CONTENT SPEAK ROBOT?</h1>
  <div class="abs rule"></div>
  <div class="abs rule-accent"></div>
  <h2 class="abs subhead">Embrace the Future of Content with Harbor Lattice</h2>

  <div class="abs intro">
    <p>In a world driven by artificial intelligence and automation, the way we create and consume content is evolving rapidly. In a year that has seen unprecedented changes and challenges, it's more crucial than ever to adapt and thrive.</p>
    <p>We work with companies like yours to prepare their content for the future, ensuring readiness for both humans and machines. With a track record of proven and award-winning strategies, cutting-edge technology, and impactful training, we empower your teams to author, manage, and publish intelligent structured content. Harbor Lattice is your end-to-end partner for unlocking your content's full potential.</p>
  </div>

  <svg class="abs chat-icon" viewBox="0 0 58 58" aria-hidden="true">
    <path d="M4 4 H44 V36 H14 L4 44 Z" fill="none" stroke="#2e3192" stroke-width="3" stroke-linejoin="round"/>
    <path d="M48 16 H54 V54 L46 46 H16 V40" fill="none" stroke="#2e3192" stroke-width="3" stroke-linejoin="round"/>
    <line x1="12" y1="14" x2="34" y2="14" stroke="#9a4f9e" stroke-width="3.5" stroke-linecap="round"/>
    <line x1="12" y1="22" x2="28" y2="22" stroke="#9a4f9e" stroke-width="3.5" stroke-linecap="round"/>
  </svg>
  <p class="abs booth">Drop by our booth and chat with one of our (human) experts.</p>

  <h3 class="abs tab">Hear from our thought leaders</h3>

  <section class="abs talks">
    <div class="timeline"></div>
    <article class="talk">
      <h4 class="talk-title">The Best of Both Worlds: How Northbrook Health Delivers Personalized Content Experiences</h4>
      <p class="talk-speaker">Daniel Reyes, Dir of Content Engineering, Northbrook Health &amp; Marcus Hale, Executive VP, Harbor Lattice</p>
      <p class="talk-time">Sunday at 11:15 a.m. - Noon</p>
    </article>
    <article class="talk">
      <h4 class="talk-title">Microcontent Pipeline to Chatbots and Voice Assistants</h4>
      <p class="talk-speaker">Owen Ridley, Principal Consultant</p>
      <p class="talk-time">Monday at 9:45 - 10:30 a.m.</p>
    </article>
    <article class="talk">
      <h4 class="talk-title">Taking The Pulse of ContentOps with a Maturity Model</h4>
      <p class="talk-speaker">Lin Arora, Information Architect</p>
      <p class="talk-time">Tuesday at 8:30 - 9:15 a.m.</p>
    </article>
  </section>

  <div class="abs collab-art" role="img" aria-label="Illustration of a person and a robot fitting purple and green puzzle pieces together"></div>

  <div class="abs services-title">
    <span class="ln left"></span>
    <span>Our Services</span>
    <span class="ln right"></span>
  </div>

  <div class="abs service" style="left:35px; top:998px;">
    <span class="service-icon"><svg width="22" height="22" viewBox="0 0 22 22"><rect x="5" y="2" width="13" height="18" rx="1" fill="none" stroke="#fff" stroke-width="1.5"/><line x1="8" y1="8" x2="15" y2="8" stroke="#fff" stroke-width="1.5"/><line x1="8" y1="12" x2="15" y2="12" stroke="#fff" stroke-width="1.5"/></svg></span>
    <span class="service-name">Engagement Through<br>Content Strategy</span>
  </div>
  <div class="abs service" style="left:253px; top:998px;">
    <span class="service-icon"><svg width="22" height="22" viewBox="0 0 22 22"><circle cx="11" cy="11" r="6" fill="none" stroke="#fff" stroke-width="1.5"/><circle cx="11" cy="11" r="2" fill="#fff"/><line x1="11" y1="1" x2="11" y2="5" stroke="#fff" stroke-width="1.5"/><line x1="11" y1="17" x2="11" y2="21" stroke="#fff" stroke-width="1.5"/><line x1="1" y1="11" x2="5" y2="11" stroke="#fff" stroke-width="1.5"/><line x1="17" y1="11" x2="21" y2="11" stroke="#fff" stroke-width="1.5"/></svg></span>
    <span class="service-name">Enrichment Through<br>Digital Transformation</span>
  </div>
  <div class="abs service" style="left:472px; top:998px;">
    <span class="service-icon"><svg width="22" height="22" viewBox="0 0 22 22"><rect x="2" y="2" width="8" height="8" fill="none" stroke="#fff" stroke-width="1.5"/><rect x="12" y="2" width="8" height="8" fill="none" stroke="#fff" stroke-width="1.5"/><rect x="2" y="12" width="8" height="8" fill="none" stroke="#fff" stroke-width="1.5"/><rect x="12" y="12" width="8" height="8" fill="none" stroke="#fff" stroke-width="1.5"/></svg></span>
    <span class="service-name">Enablement Through<br>Solution Integration</span>
  </div>
  <div class="abs service" style="left:35px; top:1056px;">
    <span class="service-icon"><svg width="22" height="22" viewBox="0 0 22 22"><rect x="3" y="2" width="16" height="10" fill="none" stroke="#fff" stroke-width="1.5"/><circle cx="5" cy="16" r="2" fill="#fff"/><circle cx="11" cy="16" r="2" fill="#fff"/><circle cx="17" cy="16" r="2" fill="#fff"/></svg></span>
    <span class="service-name">Empowerment<br>Through Training</span>
  </div>
  <div class="abs service" style="left:253px; top:1056px;">
    <span class="service-icon"><svg width="22" height="22" viewBox="0 0 22 22"><path d="M2 8 L7 5 L11 8 L15 5 L20 8 L20 13 L14 18 L8 13 L2 13 Z" fill="none" stroke="#fff" stroke-width="1.5" stroke-linejoin="round"/></svg></span>
    <span class="service-name">Enlightenment<br>Through Support</span>
  </div>

  <svg class="abs footer-band" viewBox="0 0 700 54" aria-hidden="true">
    <rect x="0" y="18" width="700" height="36" fill="#0b0b0b"/>
    <path d="M463 54 L474 10 C476 3 481 0 490 0 H700 V54 Z" fill="#2e3192"/>
    <path d="M453 54 L463 18 H467 L457 54 Z" fill="#ffffff"/>
  </svg>
  <div class="abs contact" style="left:17px;"><span class="bullet"></span>harborlattice.com</div>
  <div class="abs contact" style="left:199px;"><span class="bullet"></span>more-info@harborlattice.com</div>
  <div class="abs phone">
    <span class="phone-badge"><svg width="13" height="13" viewBox="0 0 24 24"><path d="M6.6 10.8a15 15 0 0 0 6.6 6.6l2.2-2.2a1 1 0 0 1 1-.25 11.4 11.4 0 0 0 3.6.6 1 1 0 0 1 1 1V20a1 1 0 0 1-1 1A17 17 0 0 1 3 4a1 1 0 0 1 1-1h3.5a1 1 0 0 1 1 1c0 1.25.2 2.45.6 3.6a1 1 0 0 1-.25 1z" fill="#0b0b0b"/></svg></span>
    +1 (555) 014-2290
  </div>
</main>
</body>
</html>
```